Brova Equipment Sales & Rentals

We are an independent equipment dealership located in the upstate of South Carolina. Our services include Equipment Sales, Equipment Rentals, Metal Sales, and Industrial Supplies.

I have attached our logos and a few billboards that we like as examples for inspiration. Thank you!

Phone Number 864-555-0172

Website link if you want to check out our page.
https://www.brovaequip.example

```html
<!DOCTYPE html>
<html lang="en">
<head>
<meta charset="utf-8">
<title>Brova Equipment Sales &amp; Rentals – Billboard</title>
<link href="https://fonts.googleapis.com/css2?family=Exo+2:ital,wght@0,500;0,800;1,600&display=swap" rel="stylesheet">
<style>
  :root {
    --red: #e81e26;
    --ink: #231f20;
    --band-dark: #262626;
    --white: #ffffff;
    --stage: #e8ecf1;
    --machine-red: #e4332e;
    --machine-grey: #5a5a5a;
  }
  * { box-sizing: border-box; margin: 0; padding: 0; }
  html, body {
    width: 1200px; height: 827px; overflow: hidden;
    background: var(--stage);
  }
  .billboard {
    position: absolute; left: 0; top: 134px;
    width: 1200px; height: 559px;
    background: var(--white);
    font-family: "Exo 2", sans-serif;
    overflow: hidden;
  }
  .headline {
    position: absolute; white-space: nowrap;
    font-style: italic; font-weight: 600;
    font-size: 76px; line-height: 1; letter-spacing: -0.3px;
    color: var(--ink);
  }
  .headline .accent { color: var(--red); }
  .headline--sales { left: 50px; top: 13px; }
  .headline--supplies { left: 35px; top: 93px; }
  .headline--metal { left: 20px; top: 174px; }

  .machine {
    position: absolute;
    border-radius: 14px;
  }
  .machine--loader {
    left: 4px; top: 300px; width: 228px; height: 168px;
    background: linear-gradient(160deg, var(--machine-red) 0%, #c92a27 60%, var(--machine-grey) 100%);
  }
  .machine--excavator {
    left: 985px; top: 182px; width: 210px; height: 286px;
    background: linear-gradient(200deg, var(--machine-red) 0%, #d8302b 65%, var(--machine-grey) 100%);
  }

  .brand-mark {
    position: absolute; left: 248px; top: 345px;
    width: 58px; height: 58px; background: var(--red);
  }
  .brand-name {
    position: absolute; left: 322px; top: 281px;
    font-weight: 800; font-size: 172px; line-height: 1;
    letter-spacing: 2px; color: var(--ink);
  }

  .contact-band {
    position: absolute; left: 0; top: 471px;
    width: 1200px; height: 88px;
  }
  .contact-band svg { position: absolute; inset: 0; }
  .contact-phone, .contact-web {
    position: absolute; top: 0; height: 88px;
    display: flex; align-items: center;
    color: var(--white); font-weight: 500; white-space: nowrap;
  }
  .contact-phone { left: 20px; font-size: 64px; letter-spacing: 2px; }
  .contact-web { right: 20px; font-size: 50px; }
</style>
</head>
<body>
  <main class="billboard">
    <p class="headline headline--sales"><span class="accent">EQUIPMENT</span> SALES and RENTALS</p>
    <p class="headline headline--supplies">INDUSTRIAL <span class="accent">SUPPLIES</span></p>
    <p class="headline headline--metal"><span class="accent">METAL</span> SALES</p>

    <div class="machine machine--loader" role="img" aria-label="Red wheel loader with front bucket"></div>
    <div class="machine machine--excavator" role="img" aria-label="Red wheeled excavator with raised arm and bucket"></div>

    <span class="brand-mark" aria-hidden="true"></span>
    <h1 class="brand-name">BROVA</h1>

    <footer class="contact-band">
      <svg width="1200" height="88" viewBox="0 0 1200 88" aria-hidden="true">
        <rect x="0" y="0" width="1200" height="88" fill="var(--red)"/>
        <polygon points="0,0 552,0 492,88 0,88" fill="var(--band-dark)"/>
        <polygon points="552,0 572,0 512,88 492,88" fill="var(--white)"/>
      </svg>
      <span class="contact-phone">864-555-0172</span>
      <span class="contact-web">www.brovaequip.example</span>
    </footer>
  </main>
</body>
</html>
```